Flyer DesignFESTIVE, FLORISTRY WORKSHOP

WE NEED A FLYER, TO SEND OUT TO PROSPECTIVE CUSTOMERS, TO ATTEND A ONE DAY CHRISTMAS WORKSHOP, ALL MATERIALS WILL BE SUPPLIED AND SO TO WE WILL PROVIDE REFRESHMENTS, PARTICIPIANTS JUST NEED TO BRING THIER FLORISTRY SCISSORS

ON THE DAY THE WILL PARTICIPIATE IN CREATING SEASONAL FLORISTRY DESIGNS THAT THEY CAN BRING HOME TO LAST THE FESTIVE SEASON,

MAREIKE AND LORNA WILL BE THERE WITH SOME UNIQUE IDEAS TO ENHANCE OUR CHRISTMAS FESTIVITIES. TOTAL COST FOR THE DAY IS £79.00. AND THE DATE IS 6THDECEMBER, 2014, AT THE BRAMBLEGATE HOTEL DUNMARREN, WHICH HAS ALSO A BUS LINK TO MANY OTHER AREAS, SO ENJOY YOURSELVES, GET INTO THE FESTIVE FEELING ON THIS SPECIAL OCCASION

FLOWER LOVERS THAT LIKE TO CREATE THIER OWN FLORAL DESIGNS

Hotel

Decorative

Must have
• A CHRISTMAS ATMOSPHERE, WITH A BEAUTIFUL DOOR WREATH AND TABLE DESIGN

BOTH TUTORS ON THE DAY ARE HIGHLY SKILLED, HIGHLY QUALIFIED, WITH LORNA, HAVING WON GFA WEXLEY MEDAL,
Nice to have
• BETTER WORDING THAN I HAVE GIVEN YOU

telephone number 02894412385

```html
<!DOCTYPE html>
<html lang="en">
<head>
<meta charset="utf-8">
<title>Festive Floral Arrangements Workshop</title>
<link rel="stylesheet" href="https://fonts.googleapis.com/css2?family=Playball&family=Open+Sans:wght@800&family=PT+Sans+Narrow:wght@700&display=swap">
<style>
  :root {
    --festive-red: #c9141c;
    --door-red: #b3121a;
    --leaf-green: #a3c51f;
    --bright-green: #b6d22c;
    --gold-yellow: #f8e632;
    --cream: #fdf4d2;
    --ink-outline: #5a2a10;
  }
  html, body {
    margin: 0;
    padding: 0;
    overflow: hidden;
    background: #ffffff;
  }
  .flyer {
    position: relative;
    width: 1200px;
    height: 930px;
    overflow: hidden;
    background: var(--festive-red);
    font-family: "PT Sans Narrow", "Arial Narrow", sans-serif;
    font-weight: 700;
  }
  .backdrop {
    position: absolute;
    inset: 0;
  }
  .headline-lead {
    position: absolute;
    top: 40px;
    left: 224px;
    margin: 0;
    font-family: "Open Sans", Arial, sans-serif;
    font-weight: 800;
    font-size: 47px;
    line-height: 60px;
    color: var(--gold-yellow);
    -webkit-text-stroke: 1px var(--ink-outline);
    white-space: nowrap;
  }
  .headline-title {
    position: absolute;
    top: 92px;
    left: 78px;
    width: 875px;
    margin: 0;
    font-family: "Playball", cursive;
    font-weight: 400;
    font-size: 90px;
    line-height: 110px;
    text-align: center;
    color: var(--gold-yellow);
    -webkit-text-stroke: 1.5px var(--ink-outline);
    white-space: nowrap;
  }
  .details {
    position: absolute;
    top: 218px;
    left: 547px;
    width: 620px;
    text-align: center;
    color: var(--cream);
  }
  .intro {
    margin: 0;
    font-size: 28px;
    line-height: 38px;
  }
  .tutor {
    font-variant: small-caps;
    font-size: 29px;
  }
  .workshop-name {
    margin: 24px 0 0;
    font-size: 31px;
    line-height: 38px;
    font-variant: small-caps;
    color: var(--gold-yellow);
    white-space: nowrap;
  }
  .event-info {
    margin: 19px 0 0;
    font-size: 28px;
    line-height: 35px;
  }
  .phone {
    margin: 18px 0 0;
    font-family: "Open Sans", Arial, sans-serif;
    font-weight: 800;
    font-size: 32px;
    line-height: 46px;
    letter-spacing: 6px;
    color: var(--gold-yellow);
  }
  .price {
    margin: 14px 0 0;
    font-family: "Open Sans", Arial, sans-serif;
    font-weight: 800;
    font-size: 56px;
    line-height: 76px;
    color: var(--gold-yellow);
  }
</style>
</head>
<body>
<main class="flyer">
  <svg class="backdrop" width="1200" height="930" viewBox="0 0 1200 930">
    <defs>
      <radialGradient id="wreath-tones" cx="0.5" cy="0.5" r="0.5">
        <stop offset="0" stop-color="#7a4a52"/>
        <stop offset="0.35" stop-color="#6b6a44"/>
        <stop offset="0.7" stop-color="#4f6a35"/>
        <stop offset="0.88" stop-color="#5a4a30" stop-opacity="0.75"/>
        <stop offset="1" stop-color="#b3121a" stop-opacity="0"/>
      </radialGradient>
      <radialGradient id="berry-tones" cx="0.7" cy="0.3" r="0.75">
        <stop offset="0" stop-color="#8e1a20"/>
        <stop offset="0.6" stop-color="#a8161d"/>
        <stop offset="1" stop-color="#c9141c"/>
      </radialGradient>
      <linearGradient id="door-tones" x1="0" y1="0" x2="1" y2="1">
        <stop offset="0" stop-color="#c8151e"/>
        <stop offset="1" stop-color="#a10f16"/>
      </linearGradient>
      <linearGradient id="glass-tones" x1="0" y1="0" x2="0" y2="1">
        <stop offset="0" stop-color="#b88a5a"/>
        <stop offset="1" stop-color="#9c7a52"/>
      </linearGradient>
    </defs>

    <g role="img" aria-label="Photograph of a red front door with an arched glass panel, hung with a wreath of protea, banksia and eucalyptus foliage">
      <path d="M0 0 H610 C560 200 500 380 520 560 C535 700 560 830 575 930 H0 Z" fill="url(#door-tones)"/>
      <path d="M130 215 V150 C130 60 230 0 340 0 H560 C548 90 538 160 532 215 Z" fill="url(#glass-tones)" opacity="0.55"/>
      <ellipse cx="280" cy="510" rx="265" ry="340" fill="url(#wreath-tones)"/>
    </g>

    <path d="M610 0 H860 C720 180 600 360 590 560 C585 700 610 830 625 930 H575 C560 830 535 700 520 560 C500 380 560 200 610 0 Z" fill="var(--leaf-green)"/>

    <path role="img" aria-label="Photograph of a red berry wreath with green leaves" d="M815 0 H1200 V310 C1110 300 1020 250 950 170 C900 110 850 60 815 0 Z" fill="url(#berry-tones)"/>

    <path d="M1200 750 C1160 820 1120 880 1085 930 H1200 Z" fill="var(--bright-green)"/>
  </svg>

  <h2 class="headline-lead">Learn How To Create</h2>
  <h1 class="headline-title">Festive Floral Arrangements</h1>

  <section class="details">
    <p class="intro">
      Come and join us at this festive season to<br>
      create your own Christmas decoration and<br>
      enjoy some seasonal cheer.<br>
      All materials will be supplied but bring your<br>
      own floristry scissors.<br>
      Enjoy refreshments while you work under the<br>
      expert tuition and guidance of <span class="tutor">Mareike</span> and<br>
      <span class="tutor">Lorna</span> and leave with your very own<br>
      handmade Christmas decoration.
    </p>
    <p class="workshop-name">One Day Table Center &amp; Wreath Workshop</p>
    <p class="event-info">
      Saturday, 6th December, 2014<br>
      Bramblegate Hotel, Dunmarren<br>
      To book, please call on
    </p>
    <p class="phone">02894412385</p>
    <p class="price">£79</p>
  </section>
</main>
</body>
</html>
```